Harbinger Cargo needs a business card design.

Design a double-sided business card for new freight business. On the front, would like to see our logo along with the following info:

Malcolm Strathby
CEO/FOUNDER
555-207-4163
malcolmstrathby@harbinger-cargo.example

On the reverse side, we would like to use the graphic image of our logo only without the Harbinger Cargo name.

```html
<!DOCTYPE html>
<html lang="en">
<head>
<meta charset="utf-8">
<title>Harbinger Cargo – Business Card</title>
<link rel="stylesheet" href="https://fonts.googleapis.com/css2?family=Open+Sans:wght@400;700&display=swap">
<style>
  :root {
    --navy: #231f5e;
    --navy-deep: #1b1850;
    --violet: #6b63b5;
    --red: #b3202a;
    --red-deep: #6e0f16;
    --white: #ffffff;
    --paper-shade: #ececef;
    --faint-violet: rgba(35, 31, 94, 0.09);
    --faint-red: rgba(179, 32, 42, 0.08);
    --backdrop: #d9d9dc;
  }
  * { box-sizing: border-box; margin: 0; padding: 0; }
  html, body {
    width: 1200px;
    height: 900px;
    overflow: hidden;
    background: var(--backdrop);
    font-family: "Open Sans", Arial, sans-serif;
  }
  .canvas {
    position: relative;
    width: 1200px;
    height: 900px;
  }
  .card {
    position: absolute;
    left: 250px;
    width: 700px;
    height: 400px;
    border-radius: 4px;
    box-shadow: 0 6px 18px rgba(0, 0, 0, 0.18);
    overflow: hidden;
  }

  /* Reverse side */
  .card-back {
    top: 40px;
    background: linear-gradient(135deg, var(--navy) 0%, var(--navy-deep) 100%);
  }
  .symbol-area {
    position: absolute;
    left: 80px;
    top: 110px;
    width: 380px;
    height: 250px;
    border-radius: 40px 0 0 0;
    background: linear-gradient(120deg, var(--violet) 0%, var(--red) 55%, var(--red-deep) 100%);
    opacity: 0.85;
  }
  .card-back .wordmark {
    position: absolute;
    right: 56px;
    top: 150px;
    color: var(--white);
    font-weight: 700;
    font-size: 32px;
    line-height: 1.05;
    letter-spacing: 0.18em;
    text-transform: uppercase;
  }

  /* Front side */
  .card-front {
    top: 460px;
    background: linear-gradient(100deg, var(--white) 0%, var(--white) 45%, var(--paper-shade) 100%);
  }
  .faint-symbol-area {
    position: absolute;
    right: 0;
    top: 50px;
    width: 300px;
    height: 350px;
    border-radius: 60px 0 0 0;
    background: linear-gradient(120deg, var(--faint-violet) 0%, var(--faint-red) 100%);
  }
  .card-front .wordmark {
    position: absolute;
    left: 48px;
    top: 44px;
    display: flex;
    align-items: center;
    gap: 14px;
    color: var(--navy);
    font-weight: 700;
    font-size: 30px;
    line-height: 1.05;
    letter-spacing: 0.14em;
    text-transform: uppercase;
  }
  .wordmark-square {
    width: 22px;
    height: 22px;
    background: var(--red);
    flex: none;
  }
  .contact-block {
    position: absolute;
    left: 110px;
    top: 190px;
    color: var(--navy);
  }
  .person-name {
    color: var(--red);
    font-weight: 700;
    font-size: 28px;
    line-height: 1.15;
  }
  .person-title {
    font-size: 20px;
    letter-spacing: 0.02em;
    margin-bottom: 14px;
  }
  .contact-list { list-style: none; }
  .contact-list li {
    display: flex;
    align-items: center;
    gap: 10px;
    font-size: 20px;
    line-height: 1.45;
  }
  .contact-icon {
    width: 18px;
    height: 18px;
    flex: none;
    fill: none;
    stroke: var(--red);
    stroke-width: 1.8;
  }
  .contact-icon.filled {
    fill: var(--red);
    stroke: none;
  }
</style>
</head>
<body>
<main class="canvas">

  <section class="card card-back" aria-label="Card reverse side">
    <div class="symbol-area" role="img" aria-label="Large brand symbol in violet and red"></div>
    <div class="wordmark">Harbinger<br>Cargo</div>
  </section>

  <section class="card card-front" aria-label="Card front side">
    <div class="faint-symbol-area" role="img" aria-label="Faint brand symbol watermark"></div>

    <div class="wordmark">
      <span class="wordmark-square" aria-hidden="true"></span>
      <span>Harbinger<br>Cargo</span>
    </div>

    <div class="contact-block">
      <p class="person-name">Malcolm Strathby</p>
      <p class="person-title">CEO/FOUNDER</p>
      <ul class="contact-list">
        <li>
          <svg class="contact-icon filled" viewBox="0 0 24 24" aria-hidden="true">
            <path d="M6.6 10.8a15.1 15.1 0 0 0 6.6 6.6l2.2-2.2a1 1 0 0 1 1-.25 11.4 11.4 0 0 0 3.6.57 1 1 0 0 1 1 1V20a1 1 0 0 1-1 1A17 17 0 0 1 3 4a1 1 0 0 1 1-1h3.5a1 1 0 0 1 1 1c0 1.25.2 2.45.57 3.6a1 1 0 0 1-.25 1z"/>
          </svg>
          <span>555-207-4163</span>
        </li>
        <li>
          <svg class="contact-icon" viewBox="0 0 24 24" aria-hidden="true">
            <rect x="2.5" y="5" width="19" height="14"/>
            <path d="M2.5 5l9.5 8 9.5-8M2.5 19l7-6.5M21.5 19l-7-6.5"/>
          </svg>
          <span>malcolmstrathby@harbinger-cargo.example</span>
        </li>
        <li>
          <svg class="contact-icon" viewBox="0 0 24 24" aria-hidden="true">
            <circle cx="12" cy="12" r="9.5"/>
            <path d="M2.5 12h19M12 2.5c3 3 3 16 0 19M12 2.5c-3 3-3 16 0 19M4.5 7h15M4.5 17h15"/>
          </svg>
          <span>www.harbinger-cargo.example</span>
        </li>
      </ul>
    </div>
  </section>

</main>
</body>
</html>
```